Web Design for US Hispanic Business Community

Zep Tal Group aka www.MarlowVentura.TV is a dynamic new entrant in the the Hispanic internet small business solutions and services marketplace, through - engaging easy to use start-up business solutions.

Marlow Ventura TV will feature a local online production of a weekly lifestyle show surrounded around community interest. Video news, business, Fashion and food channels and other topics around the Hispanic lifestyle trends in local Colorado area and across the US.

MVTV also provides budding Hispanic entrepreneurs a one stop shopping spot, providing access, participation and guidance including coaching, that may have been unattainable in the past, due to U.S job market shortages. For those Hispanics who want to to move into the business world and attain an improved and better quality of life.

To established sme's including e-commerce businesses and traditional retailers, MVTV will provide a platform from which to leverage Hispanic market share and brand positioning. Content on this site will also attract and engage Businesses, CEO's and budding entrepreneurs.

Solutions offered on Marlow Ventura TV

Focused and tightly targeted Audience
Strategic Marketing Solutions (sem/seo/social media)
Education and Learning
Custom Content Creation
Product Placement
How to videos
Daily Deals
CEO Corner

Objective of this web portal: Marlow Ventura TV will build a unique internet portal site, like no other and combind this with unique products and services that will guide both businesses and consumers to the site. This internet portal will be the the first point of contact for all those engaging in Marlow Ventura TV and will be the point from which users start to interact with the portal. Ideally, this will be the first point from which Hispanics in the US start all internet activity.

Design Needs (Please note this is design only, Coding/development to be done by someone else):

I will be using a Wordpress CMS so please keep this in mind.

I'll be needing design for the following 4 main pages and the 5 "templates" below. I have attached the Logo to work with. Please note the font used in the circles can be customised if you think there is a better choice.

Web Portal must have
1) Customised Home Page (creative & Original layouts PLEASE!!!
2) Customised Marketplace page (This page highlights all the products and services on offer through the site)
3) Customised Entertainment and Dining Page (with a fashionable and funky icon. This page will drive high traffic)
4)A Community Upload Page - This will be user generated content, you could potentially use the circles of the logo to mark video content (there is also potential to use one or more of the coloured circles with a little video camera beside it)

Template layouts for 5 other following pages.

5 other pages include -

News Channel, Health and Lifestyle, Fashion, Food and Recipes and Daily Deals (This could be a plugin but I'd probably still want it customised).

I have included here example of web layout I like, esp for home page(Brisk Parlor TV) http://briskparlor.tv/video-library/brisk-parlor-june-25-2012

I have attached a design map of home page design I like.

I have attached a flow chart on the content that will be uploaded on each page (Take note where RSS feeds fit in)

I have included in 'Nice to have' a link of a 'slide' that I would also like on the home page http://quillmarket.net/item/community/512847?WT.ac=category_thumb&WT.seg_1=category_thumb&WT.z_author=pebblor

Please see all attached documents and links included.
Updates

I need to see original layout concepts, Please!!!

Please make header logo Dominant...I also added an image that I think would look cool for the blogging images...

Added a couple new logo files please replace with this one. lso I created a logo for my UGC Video upload, that needs to be featured in middle of page and on the footer

Target Market(s)

25- 49 year old U.S Hispanics and those in business. Hispanic communities usage rates of Smartphones, Television, Online Video and Social networking and other forms of entertainment make this group one of todays most engaged populations in todays digital space. Following Trends of this group mean that according to Varrick reasecrh this group send 941 txt msgs a month, more then any other ethnic group and are 25% more likely to follow a brand and 18% more likely to follow a celebrity then any other online group.

Industry/Entity Type

E-Commerce

Requirements
Must have
• Must have a corporate, Tech savvy design feel (not over the top). This is a professional, but hip and fashionable site.
White Background
The ability to fit RSS video Feeds
Entertainment and Dining page must have radio box or a cool icon to customize it as fashionable entertainment page, as this page will land majority traffic.
SEE FLOW CHART ON WEB LAYOUT ATTACHED
Nice to have
• Experiment with the text color in slogan line, & font style in circles of logo.
Homepage including Slider (I have below is a link to a website that I am happy with the look of the slider on)
http://quillmarket.net/item/community/512847?WT.ac=category_thumb&WT.seg_1=category_thumb&WT.z_author=pebblor
Should not have
• Must not be cartoony or childish

6/27 Update,
I uploaded a image of slider I like at lumorava.com (video tab,check it out)I love the functionality of it-this is hm pg screen we need wow factor!, I need banners on each side if possible or a creative way to find some banner ad space. I also uploaded MVTV Logo B Colors file try using the 1st image at top of page, need to see examples with this logo as well!

```html
<!DOCTYPE html>
<html lang="en">
<head>
<meta charset="utf-8">
<title>MarlowVentura.TV – Home</title>
<link rel="stylesheet" href="https://fonts.googleapis.com/css2?family=Open+Sans:wght@400;600&family=PT+Sans+Narrow:wght@400;700&display=swap">
<style>
:root{
  --olive:#a39b2c;--olive-dark:#8a8320;
  --blue:#1f6fb0;--orange:#f08236;--orange-dark:#e0621b;
  --text:#555;--line:#dcdcdc;--panel-top:#ffffff;--panel-bot:#f2f2f2;
  --footer:#8c7e6b;--footer-text:#fff;--brown:#8b5a2b;--ink:#3a3a3a;
}
*{box-sizing:border-box;margin:0;padding:0}
html,body{width:919px;height:1200px;overflow:hidden;background:#fff}
body{font-family:"Open Sans",Arial,sans-serif;color:var(--text);font-size:9px}
.page{position:relative;width:919px;height:1200px;border-top:4px solid #3d3630}
.abs{position:absolute}
.brand{left:132px;top:40px;font-size:20px;font-weight:600;color:var(--ink);white-space:nowrap}
.search{left:626px;top:7px;width:171px;height:20px;border:1px solid #ccc;border-radius:4px;background:linear-gradient(#fff,#eee);font-size:8px;color:#333;padding:4px 9px}
.search svg{position:absolute;right:6px;top:4px}
.ad{left:466px;top:38px;width:331px;height:42px;background:linear-gradient(90deg,#1b3f8f,#2a62c4 55%,#f0c419 78%,#e74c1d);border:1px solid #1b3a7a}
.nav{left:121px;top:93px;width:676px;height:20px}
.nav a{position:absolute;top:0;height:20px;line-height:20px;text-align:center;color:#fff;font-size:8.5px;text-decoration:none;background:linear-gradient(#b7ae3a,var(--olive-dark));border-radius:2px;box-shadow:0 1px 2px rgba(0,0,0,.3)}
.car-bar{top:123px;width:14px;height:82px;background:#bdbdbd}
.car-arrow{position:absolute;top:32px;width:16px;height:16px;border-radius:50%;background:#fff;border:1px solid #999}
.thumb{top:123px;width:154px;height:82px}
.hero{left:122px;top:212px;width:428px;height:190px;background:linear-gradient(90deg,#d9d3c8,#f3eee6 45%,#c7d3e0);border:1px solid #ddd}
.panel{background:linear-gradient(var(--panel-top),var(--panel-bot));border:1px solid var(--line);border-radius:3px}
.hero-side{left:557px;top:212px;width:239px;height:190px}
.hero-side p{position:absolute;left:17px;top:14px;width:208px;font-size:8.3px;line-height:17px;color:#444}
.btn-blue{position:absolute;display:block;background:linear-gradient(#3a9ae0,#1d72bd);color:#fff;font-size:8px;text-align:center;border-radius:2px;text-decoration:none}
.video{left:653px;top:312px;width:132px;height:79px;background:linear-gradient(#6a8c4c,#2f3a2a);border:1px solid #222}
.video svg{position:absolute;left:58px;top:30px}
h2{font-family:"PT Sans Narrow",sans-serif;font-weight:400;color:var(--blue)}
.card{position:absolute}
.card h2{position:absolute;left:10px;top:6px;font-size:12.5px}
.card .rule{position:absolute;left:10px;right:10px;top:25px;border-top:1px solid var(--line)}
.card p{position:absolute;left:11px;right:12px;top:33px;font-size:8.3px;line-height:13.5px;text-align:justify}
.card .ico{position:absolute;right:10px;top:7px}
.pill{position:absolute;display:block;height:14px;line-height:14px;text-align:center;color:#fff;font-size:8.3px;text-decoration:none;border-radius:8px;background:linear-gradient(#f79a52,var(--orange-dark));box-shadow:0 1px 1px rgba(0,0,0,.25)}
.mini{position:absolute;font-size:8px;font-weight:600;color:var(--brown)}
.blog ul{list-style:none;position:absolute;top:38px;font-size:8.3px;line-height:11px}
.blog li{position:relative;padding-left:10px;margin-bottom:8px;width:190px}
.blog li:before{content:"";position:absolute;left:0;top:3px;border-left:4px solid #888;border-top:3px solid transparent;border-bottom:3px solid transparent}
.tabs a{position:absolute;top:13px;font-family:"PT Sans Narrow",sans-serif;font-size:12px;color:var(--blue);text-decoration:none}
.tabs .active{top:7px;left:6px;width:61px;height:23px;line-height:21px;border:1px solid #ccc;border-radius:3px;background:#fff;text-align:center}
.pop-item{position:absolute;left:8px;width:230px;height:59px}
.pop-item .img{position:absolute;left:0;top:0;width:77px;height:59px}
.pop-item p{position:absolute;left:84px;top:3px;width:140px;font-size:8.3px;line-height:14.5px;color:#333}
.vid-img{background:linear-gradient(90deg,#3b3a36,#7b6a58 55%,#2e2b27)}
.vid-img svg{position:absolute;left:28px;top:20px}
.check{position:absolute;width:14px;height:13px;background:#bdbdbd}
.input{position:absolute;border:1px solid #ccc;border-radius:9px;background:#fff;font-size:8.3px;color:#444;padding:4px 11px}
.footer{left:0;top:979px;width:919px;height:221px;background:var(--footer);color:var(--footer-text)}
.footer h3{position:absolute;font-family:"PT Sans Narrow",sans-serif;font-weight:400;font-size:13px}
.social{position:absolute;left:292px;font-family:"PT Sans Narrow",sans-serif;font-size:12.5px}
.social i{display:inline-block;width:21px;height:21px;border-radius:3px;vertical-align:middle;margin-right:12px}
.flinks a{position:absolute;right:141px;font-size:8.3px;color:#fff;text-decoration:none;text-align:right}
</style>
</head>
<body>
<div class="page">

  <div class="abs brand">MarlowVentura.TV</div>

  <div class="abs search">Search<svg width="11" height="11" viewBox="0 0 11 11"><circle cx="4.5" cy="4.5" r="3.3" fill="none" stroke="#777" stroke-width="1.3"/><path d="M7 7l3 3" stroke="#777" stroke-width="1.6"/></svg></div>
  <div class="abs ad" role="img" aria-label="Banner advertisement for free private label rights info products with a download button"></div>

  <nav class="abs nav">
    <a style="left:0;width:84px">NEWS CHANELS</a>
    <a style="left:93px;width:88px">HEALTH &amp; SALUD!</a>
    <a style="left:192px;width:102px">FASHION / LIFESTYLE</a>
    <a style="left:302px;width:76px">MARKETPLACE</a>
    <a style="left:386px;width:122px">ENTERTAINMENT / DINNING</a>
    <a style="left:516px;width:78px">FOOT RECEIPIES</a>
    <a style="left:601px;width:75px">DEALS</a>
  </nav>

  <div class="abs car-bar" style="left:122px"><span class="car-arrow" style="left:-1px"><svg width="14" height="14" viewBox="0 0 14 14"><path d="M8 4L5 7l3 3" fill="none" stroke="#333" stroke-width="1.6"/></svg></span></div>
  <div class="abs thumb" style="left:146px;background:linear-gradient(#c7b189,#6a8a3e 60%,#b7362b)" role="img" aria-label="Soccer players in red and blue kits on a field"></div>
  <div class="abs thumb" style="left:304px;background:linear-gradient(#9aa0a6,#4d4f55 50%,#8d8378)" role="img" aria-label="Crowd of marathon runners on a road"></div>
  <div class="abs thumb" style="left:463px;background:linear-gradient(#1c4f9e,#4f86d0 45%,#e8eef7)" role="img" aria-label="Skier carving down a snowy slope"></div>
  <div class="abs thumb" style="left:621px;background:linear-gradient(#d59b44,#4e8c63 60%,#5c8f4a)" role="img" aria-label="Field hockey players competing on a pitch"></div>
  <div class="abs car-bar" style="left:783px"><span class="car-arrow" style="left:-1px"><svg width="14" height="14" viewBox="0 0 14 14"><path d="M6 4l3 3-3 3" fill="none" stroke="#333" stroke-width="1.6"/></svg></span></div>

  <div class="abs hero" role="img" aria-label="Business advisor meeting a young couple at a desk in a bright office"></div>
  <div class="abs panel hero-side">
    <p>Lorem Ipsum is simply dummy text of the printing and typesetting industry. Lorem Ipsum has been the industry's standard dummy text ever since the 1500s, when an unknown printer took a galley of type and scrambled</p>
    <a class="btn-blue" style="left:16px;top:152px;width:63px;height:19px;line-height:19px">Read More&gt;&gt;</a>
  </div>
  <div class="abs video" role="img" aria-label="Video still of a presenter speaking to camera"><svg width="16" height="16" viewBox="0 0 16 16"><circle cx="8" cy="8" r="8" fill="#d33" opacity=".85"/><path d="M6 4.5v7l5.5-3.5z" fill="#fff"/></svg></div>

  <section class="card panel blog" style="left:123px;top:418px;width:427px;height:98px">
    <h2 style="left:9px;top:5px;font-size:15px">Blog</h2>
    <ul style="left:14px"><li>Lorem Ipsum is simply dummy text of the printing and typesetting industry.</li><li>Lorem Ipsum is simply dummy text of the printing and typesetting industry.</li></ul>
    <ul style="left:220px"><li>Lorem Ipsum is simply dummy text of the printing and typesetting industry.</li><li>Lorem Ipsum is simply dummy text of the printing and typesetting industry.</li></ul>
  </section>

  <section class="card panel" style="left:124px;top:521px;width:208px;height:105px">
    <h2>News &amp; Rss Feed</h2>
    <svg class="ico" width="15" height="15" viewBox="0 0 15 15"><rect x="1" y="3" width="11" height="11" fill="none" stroke="#222" stroke-width="1.5"/><path d="M6 9l7-7" stroke="#222" stroke-width="2"/></svg>
    <div class="rule"></div>
    <p>Lorem Ipsum is simply dummy text of the printing and typesetting industry. Lorem Ipsum has been the industry's</p>
    <a class="pill" style="left:12px;top:85px;width:67px">Net News</a>
    <a class="pill" style="left:83px;top:85px;width:66px">Local News</a>
    <span class="mini" style="left:166px;top:87px">MVTV</span>
  </section>
  <section class="card panel" style="left:341px;top:521px;width:209px;height:105px">
    <h2>Health &amp; Rss Feed</h2>
    <svg class="ico" width="15" height="16" viewBox="0 0 15 16"><circle cx="7.5" cy="4.5" r="3.5" fill="#222"/><path d="M1 16c0-6 13-6 13 0z" fill="#222"/></svg>
    <div class="rule"></div>
    <p>Lorem Ipsum is simply dummy text of the printing and typesetting industry. Lorem Ipsum has been the industry's</p>
    <span class="mini" style="left:14px;top:87px">MVTV</span>
    <a class="pill" style="left:123px;top:85px;width:78px">How to Videos</a>
  </section>

  <section class="card panel" style="left:124px;top:635px;width:208px;height:105px">
    <h2>Marketplace</h2>
    <svg class="ico" width="15" height="15" viewBox="0 0 15 15"><rect x="1" y="3" width="11" height="11" fill="none" stroke="#222" stroke-width="1.5"/><path d="M6 9l7-7" stroke="#222" stroke-width="2"/></svg>
    <div class="rule"></div>
    <p>Lorem Ipsum is simply dummy text of the printing and typesetting industry. Lorem Ipsum has been the industry's</p>
    <a class="pill" style="left:12px;top:85px;width:75px">How to Video</a>
    <span class="mini" style="left:166px;top:87px">MVTV</span>
  </section>
  <section class="card panel" style="left:341px;top:635px;width:209px;height:105px">
    <h2>Daily Deals</h2>
    <svg class="ico" width="15" height="15" viewBox="0 0 15 15"><rect x="1" y="3" width="11" height="11" fill="none" stroke="#222" stroke-width="1.5"/><path d="M6 9l7-7" stroke="#222" stroke-width="2"/></svg>
    <div class="rule"></div>
    <p>Lorem Ipsum is simply dummy text of the printing and typesetting industry. Lorem Ipsum has been the industry's</p>
    <a class="pill" style="left:13px;top:85px;width:43px">Plugin</a>
    <span class="mini" style="left:166px;top:87px">MVTV</span>
  </section>

  <section class="card panel" style="left:557px;top:418px;width:239px;height:322px">
    <div class="tabs"><a class="active">Popular</a><a style="left:86px">Recent</a><a style="left:135px">Comments</a><a style="left:199px">Tags</a></div>
    <div class="pop-item" style="top:46px"><div class="img" style="background:linear-gradient(90deg,#4b4f48,#b6aa94 50%,#e7e1d6)" role="img" aria-label="Colleagues greeting each other in an office"></div><p>Lorem Ipsum is simply dummy text of the printing and typeset-ting industry.</p></div>
    <div class="pop-item" style="top:114px"><div class="img vid-img" role="img" aria-label="Video still of a presenter"><svg width="20" height="20" viewBox="0 0 20 20"><circle cx="10" cy="10" r="10" fill="#c9302c" opacity=".85"/><path d="M8 6v8l6-4z" fill="#fff"/></svg></div><p>Lorem Ipsum is simply dummy text of the printing and typeset-ting industry.</p></div>
    <div class="pop-item" style="top:182px"><div class="img vid-img" role="img" aria-label="Video still of a presenter"><svg width="20" height="20" viewBox="0 0 20 20"><circle cx="10" cy="10" r="10" fill="#c9302c" opacity=".85"/><path d="M8 6v8l6-4z" fill="#fff"/></svg></div><p style="left:87px">Lorem Ipsum is simply dummy text of the printing and typeset-ting industry.</p></div>
    <div class="pop-item" style="top:250px"><div class="img vid-img" role="img" aria-label="Video still of a presenter"><svg width="20" height="20" viewBox="0 0 20 20"><circle cx="10" cy="10" r="10" fill="#c9302c" opacity=".85"/><path d="M8 6v8l6-4z" fill="#fff"/></svg></div><p style="left:87px">Lorem Ipsum is simply dummy text of the printing and typeset-ting industry.</p></div>
  </section>

  <section class="card panel" style="left:123px;top:753px;width:427px;height:128px">
    <h2 style="left:8px;top:5px">Entertainment / Dining RSS Feed</h2>
    <div class="rule" style="left:8px;right:10px"></div>
    <p style="left:10px;right:10px;top:33px;font-size:8.1px">Lorem Ipsum is simply dummy text of the printing and typesetting industry. Lorem Ipsum has been the industry's standard dummy text ever since the 1500s, when an unknown printer took a galley of type and scrambled it to make a type specimen book. It has survived not only five centuries, but also the leap into electronic typesetting.</p>
    <a class="pill" style="left:8px;top:92px;width:120px;height:30px;line-height:11px;padding-top:4px;border-radius:14px">Night Screen Restuarant &amp;<br>Nightclub Reviews</a>
    <a class="pill" style="left:133px;top:97px;width:92px;height:18px;line-height:18px">Local Event Calender</a>
    <a class="pill" style="left:231px;top:97px;width:69px;height:18px;line-height:18px">How to Video</a>
  </section>

  <section class="card panel" style="left:557px;top:753px;width:239px;height:128px">
    <a class="pill" style="left:6px;top:6px;width:71px;height:18px;line-height:18px;border-radius:4px">Subscribe Now</a>
    <p style="left:10px;right:10px;top:35px;font-size:8.3px;line-height:11px;text-align:left">Select the newsletter to which you want to subscribe or unsubscribe</p>
    <span class="check" style="left:12px;top:69px"></span>
    <span class="input" style="left:33px;top:68px;width:193px;height:19px">Newsletter</span>
    <span class="check" style="left:12px;top:94px"></span>
    <span class="mini" style="left:36px;top:95px">MVTV</span>
    <a class="pill" style="left:110px;top:106px;width:59px;height:16px;line-height:16px">Subscribe</a>
    <a class="pill" style="left:173px;top:106px;width:60px;height:16px;line-height:16px">Unsubscribe</a>
  </section>

  <section class="card panel" style="left:124px;top:890px;width:208px;height:84px">
    <h2>Fashion / Lifestyle RSS Feed</h2>
    <div class="rule"></div>
    <p>Lorem Ipsum is simply dummy text of the printing and typesetting industry.</p>
    <a class="pill" style="left:10px;top:62px;width:72px">How to Video</a>
    <a class="pill" style="left:85px;top:62px;width:91px">Beauty &amp; Fashion Tips</a>
  </section>
  <section class="card panel" style="left:341px;top:890px;width:209px;height:84px">
    <h2>Food / Recipies, RSS Feed</h2>
    <div class="rule"></div>
    <p>Lorem Ipsum is simply dummy text of the printing and typesetting industry.</p>
    <a class="pill" style="left:10px;top:62px;width:72px">How to Video</a>
  </section>

  <footer class="abs footer">
    <div class="abs" style="left:142px;top:78px;font-size:14px;font-weight:600;color:#fff;white-space:nowrap">MarlowVentura.TV</div>
    <h3 style="left:292px;top:15px">Connect With Us</h3>
    <div class="social" style="top:47px"><i style="background:#2a6ea8"></i>Netlink</div>
    <div class="social" style="top:75px"><i style="background:#4aa8de"></i>Chirper</div>
    <div class="social" style="top:104px"><i style="background:#3a5a98"></i>Friendbook</div>
    <div class="social" style="top:131px"><i style="background:#f08a24"></i>RSS</div>
    <h3 style="left:409px;top:15px">Most Viewed</h3>
    <div class="abs" style="left:411px;top:41px;width:86px;height:46px;background:linear-gradient(#c7b189,#6a8a3e 60%,#b7362b)" role="img" aria-label="Soccer players on a field"></div>
    <div class="abs" style="left:510px;top:41px;width:87px;height:46px;background:linear-gradient(#9aa0a6,#4d4f55 50%,#8d8378)" role="img" aria-label="Marathon runners on a road"></div>
    <h3 style="left:413px;top:99px">Members Generated Video Upload</h3>
    <div class="abs" style="left:648px;top:21px;width:134px;height:19px;border-radius:8px;background:#fff;color:#888;font-size:11px;font-family:'PT Sans Narrow',sans-serif;padding:2px 7px">Search</div>
    <div class="flinks">
      <a style="top:58px">About Us</a><a style="top:80px">Archieve</a><a style="top:101px">Newsletters</a><a style="top:122px">Advertise</a><a style="top:143px">Contact</a><a style="top:164px">Site Map</a>
    </div>
    <div class="abs" style="left:130px;top:186px;width:652px;border-top:1px solid #6f6353"></div>
    <div class="abs" style="left:0;top:196px;width:878px;text-align:center;font-size:8.3px">Copyrights @ 2012 All Rights Reserved</div>
  </footer>
</div>
</body>
</html>
```